Killer design for artists website and gallery

Current website is www.pebblenook.com.au and it runs on a very simple Wordpress standard theme. We would like a theme designed and customised to suit the branding and style. We have someone who will then code the site in HTML and CSS into Wordpress.

The general theme and branding can be seen on the site at the moment. Please note I have now uploaded full size files into the project. The website background files are for reference only as they are currently on the site. There is no requirement to use them in the new design, however the logo must be as per the attachment.. Please submit a home page/main gallery, and we will request additional pages (about us, other galleries etc.) from those designers we like during the project time.
Updates

Please note I have now uploaded full size files into the project. The website background files are for reference only as they are currently on the site. There is no requirement to use them in the new design, however the logo must be as per the attachment.

Target Market(s)

sales are only in Australia, and priced between approx $100 and $1000. Most viewers and buyers are 20-40 years old, and looking for a casual canvas work for home, or a gift.

Industry/Entity Type

Artists

Font styles to use
Serif
Sans Serif

Requirements
Must have
• gallery of images, responsive design, ability to select categories of pictures (see top menu on current site) and have the gallery change to match, colours to match branding and logo.
Nice to have
• simple minimalist style is preferred. More like http://www.tobiasmerlowe.com/ than http://www.harborcanvasco.com.au/ or http://www.vividplume.com.au/
Should not have
• does not need any online store, or shopping cart etc.

```html
<!DOCTYPE html>
<html lang="en">
<head>
<meta charset="utf-8">
<title>Pebble Nook – Canvas Art Made in Melbourne</title>
<link href="https://fonts.googleapis.com/css2?family=Raleway:wght@400;500&family=Open+Sans:wght@400;600;700&family=Crimson+Text:wght@400&display=swap" rel="stylesheet">
<style>
:root{
  --page:#f5f4f2;
  --white:#ffffff;
  --ink:#333333;
  --body:#555555;
  --nav:#666666;
  --rule:#e2e0dc;
  --link:#2b7fc4;
  --logo:#141210;
  --logo-text:#f3e9c8;
  --bar:#e3e2df;
  --black:#111111;
  --s1:#3b5998;
  --s2:#3aa0e0;
  --s3:#f08a24;
  --s4:#d9402f;
  --s5:#c8202a;
}
*{margin:0;padding:0;box-sizing:border-box}
html,body{width:929px;height:1200px;overflow:hidden}
body{position:relative;background:var(--page);font-family:"Open Sans",Arial,sans-serif;color:var(--body)}
.abs{position:absolute}
.site-header{left:0;top:0;width:929px;height:87px;background:var(--white);border-bottom:1px solid var(--rule)}
.brand{left:116px;top:8px;width:72px;height:72px;background:var(--logo);border-radius:6px;display:flex;align-items:flex-end;justify-content:center;padding-bottom:12px}
.brand span{font-family:"Open Sans",Arial,sans-serif;font-size:9.5px;font-weight:400;color:var(--logo-text);white-space:nowrap;letter-spacing:.3px}
.social{display:flex;gap:7px}
.social i{display:block;width:15px;height:15px;border-radius:1px}
.social i:nth-child(1){background:var(--s1)}
.social i:nth-child(2){background:var(--s2)}
.social i:nth-child(3){background:var(--s3)}
.social i:nth-child(4){background:var(--s4)}
.social i:nth-child(5){background:var(--s5)}
.social-top{left:711px;top:14px}
.main-nav{right:117px;top:57px;display:flex;gap:18px;font-family:"Raleway",Arial,sans-serif;font-size:12px;color:var(--nav);white-space:nowrap}
.main-nav .current{color:var(--ink);font-weight:500}
.gallery{left:116px;top:104px;width:696px;height:639px;background:var(--white)}
.feature{left:15px;top:15px;width:667px;height:481px;background:linear-gradient(180deg,#9c9ccc 0%,#b4afd6 30%,#c7bfdc 47%,#8fc7d8 52%,#2fb0cc 58%,#2c9fbd 66%,#d89a3a 72%,#c4623a 80%,#7a5a3a 90%,#b97a3e 100%)}
.thumb{top:511px;width:99px}
.thumb .art{width:99px;height:99px}
.thumb p{margin-top:4px;font-size:11.5px;font-weight:700;color:var(--ink)}
.arrow{top:552px}
.intro{left:105px;top:776px;width:718px;text-align:center}
.intro h1{display:flex;align-items:center;gap:8px;font-family:"Crimson Text",Georgia,serif;font-weight:400;font-size:20px;color:var(--ink);white-space:nowrap;margin:0 11px}
.intro h1::before,.intro h1::after{content:"";flex:1;border-top:3px double var(--rule)}
.intro p{font-size:10.8px;line-height:16.5px;margin:6px auto 15px;letter-spacing:-.05px}
.intro a{color:var(--link);text-decoration:none}
.divider{left:40px;top:953px;width:853px;border-top:1px solid var(--rule)}
.widget h2{font-family:"Crimson Text",Georgia,serif;font-weight:400;font-size:19.5px;color:var(--ink);margin-bottom:4px}
.widget ul{list-style:none;font-size:11px;color:var(--body)}
.widget li{line-height:21.7px}
.posts li{line-height:13px;margin:4px 0 9px}
.follow p{font-size:10.6px;line-height:15px;margin-left:1px;letter-spacing:-.1px}
.follow .field{width:234px;height:24px;background:var(--white);border:1px solid var(--rule);margin:7px 0 9px 1px}
.follow .count{font-family:"Crimson Text",Georgia,serif;font-size:13px;color:var(--ink);margin-bottom:8px}
.follow .btn{display:inline-block;background:var(--black);color:var(--white);font-family:"Crimson Text",Georgia,serif;font-size:12.5px;padding:1px 7px 2px;margin-left:1px}
.site-footer{left:0;top:1165px;width:929px;height:35px;background:var(--bar)}
.site-footer small{position:absolute;left:116px;top:13px;font-size:10px;color:var(--ink)}
.social-bottom{right:117px;top:11px;position:absolute}
</style>
</head>
<body>
<header class="site-header abs">
  <div class="brand abs"><span>PEBBLE NOOK</span></div>
  <div class="social social-top abs"><i></i><i></i><i></i><i></i><i></i></div>
  <nav class="main-nav abs">
    <span class="current">Home</span><span>About</span><span>Cityscapes</span><span>Other Works</span><span>Seascapes</span><span>Testimonials</span><span>Works for Sale</span>
  </nav>
</header>

<section class="gallery abs">
  <div class="feature abs" role="img" aria-label="Featured painting: colourful surfboards leaning on a beach fence by the sea"></div>
  <svg class="arrow abs" style="left:2px" width="10" height="14" viewBox="0 0 10 14"><path d="M8 1 2 7l6 6" fill="none" stroke="#bbb" stroke-width="2"/></svg>
  <svg class="arrow abs" style="left:686px" width="10" height="14" viewBox="0 0 10 14"><path d="M2 1l6 6-6 6" fill="none" stroke="#bbb" stroke-width="2"/></svg>
  <div class="thumb abs" style="left:15px"><div class="art" role="img" aria-label="Painting of a beach umbrella on the shore" style="background:linear-gradient(180deg,#2f6a7a 0%,#4f9aa0 45%,#9fc0b0 58%,#e0b670 70%,#d39a55 100%)"></div><p>Art</p></div>
  <div class="thumb abs" style="left:129px"><div class="art" role="img" aria-label="Painting of surfboards by a fence" style="background:linear-gradient(180deg,#a9a8d4 0%,#c5bedc 40%,#3fb2cc 55%,#e0a63a 70%,#c85a3a 85%,#8a6a44 100%)"></div><p>Other Work</p></div>
  <div class="thumb abs" style="left:243px"><div class="art" role="img" aria-label="Painting of a city market arcade" style="background:linear-gradient(135deg,#e8c84a 0%,#b88a3a 35%,#7a5036 60%,#4a6a9a 85%,#c8d4e0 100%)"></div><p>Market</p></div>
  <div class="thumb abs" style="left:356px"><div class="art" role="img" aria-label="Painting of a cathedral and city street" style="background:linear-gradient(180deg,#f6c45a 0%,#f0a24a 35%,#b88a66 60%,#7a6656 80%,#4a4040 100%)"></div><p>Cityscapes</p></div>
  <div class="thumb abs" style="left:469px"><div class="art" role="img" aria-label="Painting of boats on a calm bay" style="background:linear-gradient(180deg,#2a3a9a 0%,#7a8ad0 30%,#d8d8ec 50%,#3a8ad0 62%,#1e5aa8 100%)"></div><p>Seascapes</p></div>
  <div class="thumb abs" style="left:583px"><div class="art" role="img" aria-label="Painting of beach bathing boxes" style="background:linear-gradient(180deg,#8ec6e6 0%,#b8d8ea 30%,#c86a5a 45%,#7a8aa0 65%,#e0b07a 80%,#d88a4a 100%)"></div><p>Social</p></div>
</section>

<section class="intro abs">
  <h1>Beautiful Canvas art Made in Melbourne</h1>
  <p>Clara Penhale is a local artist who paints with acrylics, specialising in seascapes, landscapes and cityscapes. She has painted for many years and<br>studied under established artists in Melbourne.</p>
  <p>Pebble Nook was established in 2012 by Clara. The website <a>http://www.pebblenook.com.au</a> and page <a>http://www.pinboard.com/pebblenook</a> showcase<br>all recent paintings. Commissions are available along with other pieces for sale.</p>
  <p>Pebble Nook regularly holds market stalls in and around Melbourne. Details for all upcoming markets are posted on both the website and Pinboard.</p>
</section>

<div class="divider abs"></div>

<aside class="widget abs" style="left:116px;top:986px">
  <h2>Meta</h2>
  <ul><li>Register</li><li>Log in</li><li>Entries RSS</li><li>Comments RSS</li><li>Blog at Pressleaf.com.</li></ul>
</aside>
<aside class="widget posts abs" style="left:340px;top:986px;width:150px">
  <h2>Recent Posts</h2>
  <ul><li>North Melbourne Markets</li><li>Ready for North Melbourne Market Tomorrow</li><li>Wood and Trees</li><li>Into The Rain</li><li>My newest seascape</li></ul>
</aside>
<aside class="widget follow abs" style="left:578px;top:986px;width:240px">
  <h2>Follow Blog via Email</h2>
  <p>Enter your email address to follow this blog and<br>receive notifications of new posts by email.</p>
  <div class="field"></div>
  <div class="count">Join 14 other followers</div>
  <span class="btn">Follow</span>
</aside>

<footer class="site-footer abs">
  <small>Copyright © 2014 pebblenook.com.au.&nbsp; All Rights Reserved.</small>
  <div class="social social-bottom"><i></i><i></i><i></i><i></i><i></i></div>
</footer>
</body>
</html>
```